New Logo design and Business cards

We are changing our business name and require a new Logo and business card design. Our new name will be "Evergrove Garden Design & Construction" with a focus on enhancing our clients lifestyle through correct landscape design and construction of the designed landscape. We are a full service design to construct business meaning we take care of all aspects of designing and creating your ideal outdoor spaces. To see our current work and get a feel for what we do you can go to www.tallpinegardens.com.au. We do not wish to have a major change to the website only the name/logo should change with all current colours etc being used in the new logo and business card. For our Logo I want the logo to reflect who we now are, and what we do, however I want it to have minimal impact on the website with the aim to only need to change the Logo and not colours or text styles. With the business card I need there to be a strong link between the card and the website with colours and looks being similar. I would love to see an image of one of our projects to be included on the card even as a backdrop. I have included a photo that I think could be used in the background of the business card. I have attached a copy of our current business cards (so you with have all relevant information required on the new cards) though I do want a fresh look with strong links to our website. Please feel free to contact me if you have any questions or ideas.

Construction

Evergrove Garden Design & Construction-Bringing outdoor living home.

```html
<!DOCTYPE html>
<html lang="en">
<head>
<meta charset="utf-8">
<title>Evergrove Garden Design &amp; Construction – Business Card</title>
<link rel="stylesheet" href="https://fonts.googleapis.com/css2?family=Fredoka:wght@600&family=Mulish:wght@400;700&display=swap">
<style>
  :root {
    --page: #e9e4dc;
    --coral: #ef6a55;
    --coral-soft: rgba(239,106,85,0.78);
    --ink: #050505;
    --white: #ffffff;
    --sky: #1f44a8;
    --sky-deep: #0f1c3a;
    --pool: #2f6fe0;
    --timber: #9a6238;
    --sofa: #a8927c;
    --card-w: 855px;
    --card-h: 492px;
  }
  * { box-sizing: border-box; margin: 0; padding: 0; }
  html, body { width: 1165px; height: 1200px; overflow: hidden; }
  body {
    background: var(--page);
    font-family: "Mulish", "Century Gothic", sans-serif;
    color: var(--white);
    position: relative;
  }
  .card {
    position: absolute;
    left: 155px;
    width: var(--card-w);
    height: var(--card-h);
    border: 3px solid var(--coral);
    background: var(--ink);
    overflow: hidden;
  }
  .card--front { top: 138px; }
  .card--back { top: 672px; }

  /* Front */
  .project-photo {
    position: absolute; left: 0; top: 0; width: 100%; height: 307px;
    background:
      linear-gradient(90deg, rgba(0,0,0,0) 62%, var(--coral-soft) 76%, rgba(239,106,85,0.85) 100%),
      linear-gradient(180deg, rgba(0,0,0,0) 0%, rgba(0,0,0,0) 62%, rgba(168,146,124,0.85) 78%, rgba(110,96,84,0.95) 100%),
      linear-gradient(180deg, rgba(0,0,0,0) 56%, rgba(47,111,224,0.9) 60%, rgba(47,111,224,0.9) 66%, rgba(0,0,0,0) 70%),
      linear-gradient(180deg, var(--timber) 0%, #6b4428 10%, var(--sky) 22%, #2e5fc4 48%, var(--sky-deep) 56%);
  }
  .identity {
    position: absolute; left: 0; top: 307px; width: 506px; height: 150px;
    text-align: center; padding-top: 44px;
  }
  .identity__name {
    font-family: "Fredoka", sans-serif; font-weight: 600;
    font-size: 44px; color: var(--coral);
    -webkit-text-stroke: 1.5px var(--white);
    line-height: 1;
  }
  .identity__rule {
    width: 238px; margin: 6px auto 0; border-top: 1.5px dashed var(--white);
  }
  .identity__role { font-size: 21px; margin-top: 2px; }
  .divider {
    position: absolute; left: 578px; top: 317px; width: 2px; height: 140px;
    background: linear-gradient(180deg, transparent, var(--white), transparent);
  }
  .contacts {
    position: absolute; left: 596px; top: 334px; list-style: none;
  }
  .contacts li {
    display: flex; align-items: center; gap: 8px;
    font-size: 13.5px; height: 31px; font-weight: 700;
  }
  .contacts svg { width: 20px; height: 20px; flex: none; }
  .registrations {
    position: absolute; left: 0; bottom: 6px; width: 100%;
    text-align: center; font-size: 12px; font-weight: 700; white-space: nowrap;
  }

  /* Back */
  .project-photo--dim {
    position: absolute; inset: 0;
    background:
      radial-gradient(circle at 78% 45%, rgba(239,106,85,0.28) 0%, rgba(239,106,85,0.12) 22%, rgba(0,0,0,0) 40%),
      radial-gradient(ellipse at 30% 30%, rgba(31,68,168,0.25) 0%, rgba(0,0,0,0) 45%),
      linear-gradient(180deg, #1a120d 0%, #0c1224 35%, #0d0f16 65%, #120c0a 100%);
  }
  .brand {
    position: absolute; left: 110px; top: 130px; width: 420px;
    display: flex; align-items: center; gap: 22px;
  }
  .brand__mark {
    width: 84px; height: 84px; border-radius: 50%; background: var(--coral); flex: none;
  }
  .brand__name {
    font-family: "Fredoka", sans-serif; font-weight: 600;
    font-size: 42px; color: var(--coral); line-height: 1.1;
  }
</style>
</head>
<body>

<section class="card card--front" aria-label="Business card front">
  <div class="project-photo" role="img" aria-label="Evening photo of a covered outdoor lounge deck beside a lit swimming pool, with a coral tint on the right"></div>

  <div class="identity">
    <h1 class="identity__name">Dana Moreton</h1>
    <div class="identity__rule"></div>
    <p class="identity__role">(Director)</p>
  </div>

  <div class="divider"></div>

  <ul class="contacts">
    <li>
      <svg viewBox="0 0 20 20" aria-hidden="true"><circle cx="10" cy="10" r="9" fill="none" stroke="#fff" stroke-width="1.3"/><rect x="5" y="6.5" width="10" height="7" fill="none" stroke="#fff" stroke-width="1.2"/><path d="M5 6.5l5 4 5-4" fill="none" stroke="#fff" stroke-width="1.2"/></svg>
      04 120 48 371
    </li>
    <li>
      <svg viewBox="0 0 20 20" aria-hidden="true"><circle cx="10" cy="10" r="9" fill="none" stroke="#fff" stroke-width="1.3"/><rect x="6" y="8" width="8" height="6" rx="1" fill="#fff"/><rect x="7.5" y="5.5" width="5" height="3" fill="none" stroke="#fff" stroke-width="1"/></svg>
      07 3904 1186
    </li>
    <li>
      <svg viewBox="0 0 20 20" aria-hidden="true"><circle cx="10" cy="10" r="9" fill="none" stroke="#fff" stroke-width="1.3"/><path d="M7 5.5c-1 .5-1.5 1.5-1 3 1 3 3 5 6 6 1.5.5 2.5 0 3-1l-2-1.8-1.2.8c-1.2-.6-2.2-1.6-2.8-2.8l.8-1.2z" fill="#fff"/></svg>
      dana@tallpinegardens.com.au
    </li>
    <li>
      <svg viewBox="0 0 20 20" aria-hidden="true"><circle cx="10" cy="10" r="9" fill="none" stroke="#fff" stroke-width="1.3"/><circle cx="10" cy="10" r="5.5" fill="#fff"/><path d="M7 8c1 0 2 1 1.5 2s1 1.5 0 3M12 6.5c0 1.5 1.5 1.5 1.5 3" stroke="#000" stroke-width="1" fill="none"/></svg>
      tallpinegardens.com.au/
    </li>
  </ul>

  <p class="registrations">ABN 52 614 287 903 | ACN 614 287 903 | Building Lic No. 24 81902 | Trade Guild No. 40873 | Garden Assoc. No. 527 | Design Inst. No. 648</p>
</section>

<section class="card card--back" aria-label="Business card back">
  <div class="project-photo--dim" role="img" aria-label="Darkened evening photo of the outdoor lounge deck used as a backdrop"></div>
  <div class="brand">
    <span class="brand__mark" aria-hidden="true"></span>
    <p class="brand__name">Evergrove Garden Design &amp; Construction</p>
  </div>
</section>

</body>
</html>
```